Mesh Banner Design for Business Premises

We require the design of a large mesh banner to be installed across the front fence of our warehouse. The banner should prominently feature our existing Trelborn logo and brand colours (yellow, white, and black) and be designed to be highly visible from the road.

The overall aesthetic should be strong, masculine, and industrial, reflecting the nature of the scaffolding and construction industry. The background should be predominantly black, with our branding incorporated in yellow and white for strong contrast and readability.

The banner should clearly communicate the full scope of services we provide, including:

Scaffold Design
Scaffold Engineering
Scaffold Installation / Erection
Scaffold Dismantling

It should also indicate the types of projects and clients we service, including:

Commercial
Industrial
Residential
Civil

The design should feel bold and professional, with a construction-oriented style that aligns with the scaffolding industry. It should be clean, impactful, and easy to read from a distance, ensuring passing traffic can quickly understand our services.

Where possible, subtle industrial or structural design elements (such as scaffold components, steel textures, or linework) may be incorporated into the background to reinforce the industry theme while keeping the layout uncluttered.

The final design will be produced as a large-format mesh banner for outdoor installation, so it should be created with this application and viewing distance in mind.

```html
<!DOCTYPE html>
<html lang="en">
<head>
<meta charset="utf-8">
<title>Trelborn Mesh Banner</title>
<link rel="stylesheet" href="https://fonts.googleapis.com/css2?family=Bebas+Neue&family=Montserrat:wght@600;700;800&display=swap">
<style>
  :root {
    --banner-black: #232323;
    --brand-yellow: #f8ab17;
    --brand-white: #ffffff;
    --page-bg: #ffffff;
    --caption-ink: #1c1c1c;
  }
  * { margin: 0; padding: 0; box-sizing: border-box; }
  html, body {
    width: 1200px;
    height: 2400px;
    overflow: hidden;
    background: var(--page-bg);
  }
  .sheet { position: relative; width: 1200px; height: 2400px; }

  .banner-slot { position: absolute; left: 0; width: 1200px; height: 598px; }
  .banner-slot--hero { top: 0; }
  .banner-slot--install { top: 930px; left: 134px; transform: scale(0.777); transform-origin: 0 0; }
  .banner-slot--detail { top: 1600px; }

  .banner {
    position: relative;
    width: 1200px;
    height: 598px;
    background-color: var(--banner-black);
    overflow: hidden;
  }
  .banner-speckle {
    position: absolute;
    left: 0; top: 0;
    width: 660px; height: 598px;
    background-image:
      radial-gradient(circle, rgba(248,171,23,0.55) 0 1.2px, transparent 1.6px),
      radial-gradient(circle, rgba(248,171,23,0.40) 0 1px, transparent 1.4px),
      radial-gradient(circle, rgba(248,171,23,0.30) 0 1.6px, transparent 2px);
    background-size: 37px 29px, 23px 41px, 61px 53px;
    background-position: 5px 9px, 14px 3px, 27px 18px;
    -webkit-mask-image: linear-gradient(160deg, #000 0%, rgba(0,0,0,0.6) 45%, transparent 85%);
            mask-image: linear-gradient(160deg, #000 0%, rgba(0,0,0,0.6) 45%, transparent 85%);
    pointer-events: none;
  }
  .service-tag {
    position: absolute;
    left: 68px;
    top: 53px;
    width: 330px;
    height: 90px;
    background: var(--brand-yellow);
    color: var(--banner-black);
    font-family: "Bebas Neue", "Oswald", sans-serif;
    font-size: 92px;
    line-height: 98px;
    text-align: center;
    letter-spacing: 1px;
  }
  .service-list {
    position: absolute;
    left: 0;
    top: 164px;
    list-style: none;
  }
  .service-item {
    display: flex;
    align-items: center;
    height: 82.5px;
  }
  .service-chevron {
    width: 52px;
    height: 60px;
    flex: none;
  }
  .service-name {
    margin-left: 17px;
    color: var(--brand-white);
    font-family: "Bebas Neue", "Oswald", sans-serif;
    font-size: 94px;
    line-height: 1;
    letter-spacing: 6px;
    padding-top: 8px;
  }
  .brand {
    position: absolute;
    left: 640px;
    top: 240px;
    width: 500px;
    display: flex;
    align-items: center;
    justify-content: center;
    gap: 26px;
  }
  .brand-square {
    width: 52px;
    height: 52px;
    background: var(--brand-yellow);
    flex: none;
  }
  .brand-name {
    color: var(--brand-white);
    font-family: "Montserrat", sans-serif;
    font-weight: 800;
    font-size: 50px;
    letter-spacing: 12px;
    line-height: 1;
  }
  .sector-list {
    position: absolute;
    left: 63px;
    top: 516px;
    width: 1072px;
    display: flex;
    justify-content: space-between;
    color: var(--brand-yellow);
    font-family: "Montserrat", sans-serif;
    font-weight: 800;
    font-size: 35px;
    letter-spacing: 2px;
    line-height: 40px;
    white-space: nowrap;
  }
  .presentation-note {
    position: absolute;
    left: 0;
    top: 2302px;
    width: 1200px;
    text-align: center;
    color: var(--caption-ink);
    font-family: "Montserrat", sans-serif;
    font-weight: 600;
    font-size: 22px;
    line-height: 30px;
  }
</style>
</head>
<body>
<main class="sheet">

  <div class="banner-slot banner-slot--hero">
    <section class="banner">
      <div class="banner-speckle"></div>
      <div class="service-tag">Scaffold</div>
      <ul class="service-list">
        <li class="service-item"><svg class="service-chevron" viewBox="0 0 52 60"><polyline points="-4,6 40,30 -4,54" fill="none" stroke="#f8ab17" stroke-width="13"/></svg><span class="service-name">Design</span></li>
        <li class="service-item"><svg class="service-chevron" viewBox="0 0 52 60"><polyline points="-4,6 40,30 -4,54" fill="none" stroke="#f8ab17" stroke-width="13"/></svg><span class="service-name">Engineering</span></li>
        <li class="service-item"><svg class="service-chevron" viewBox="0 0 52 60"><polyline points="-4,6 40,30 -4,54" fill="none" stroke="#f8ab17" stroke-width="13"/></svg><span class="service-name">Installation</span></li>
        <li class="service-item"><svg class="service-chevron" viewBox="0 0 52 60"><polyline points="-4,6 40,30 -4,54" fill="none" stroke="#f8ab17" stroke-width="13"/></svg><span class="service-name">Dismantling</span></li>
      </ul>
      <div class="brand"><span class="brand-square"></span><span class="brand-name">TRELBORN</span></div>
      <div class="sector-list"><span>COMMERCIAL</span><span>•</span><span>INDUSTRIAL</span><span>•</span><span>RESIDENTIAL</span><span>•</span><span>CIVIL</span></div>
    </section>
  </div>

  <div class="banner-slot banner-slot--install">
    <section class="banner">
      <div class="banner-speckle"></div>
      <div class="service-tag">Scaffold</div>
      <ul class="service-list">
        <li class="service-item"><svg class="service-chevron" viewBox="0 0 52 60"><polyline points="-4,6 40,30 -4,54" fill="none" stroke="#f8ab17" stroke-width="13"/></svg><span class="service-name">Design</span></li>
        <li class="service-item"><svg class="service-chevron" viewBox="0 0 52 60"><polyline points="-4,6 40,30 -4,54" fill="none" stroke="#f8ab17" stroke-width="13"/></svg><span class="service-name">Engineering</span></li>
        <li class="service-item"><svg class="service-chevron" viewBox="0 0 52 60"><polyline points="-4,6 40,30 -4,54" fill="none" stroke="#f8ab17" stroke-width="13"/></svg><span class="service-name">Installation</span></li>
        <li class="service-item"><svg class="service-chevron" viewBox="0 0 52 60"><polyline points="-4,6 40,30 -4,54" fill="none" stroke="#f8ab17" stroke-width="13"/></svg><span class="service-name">Dismantling</span></li>
      </ul>
      <div class="brand"><span class="brand-square"></span><span class="brand-name">TRELBORN</span></div>
      <div class="sector-list"><span>COMMERCIAL</span><span>•</span><span>INDUSTRIAL</span><span>•</span><span>RESIDENTIAL</span><span>•</span><span>CIVIL</span></div>
    </section>
  </div>

  <div class="banner-slot banner-slot--detail">
    <section class="banner">
      <div class="banner-speckle"></div>
      <div class="service-tag">Scaffold</div>
      <ul class="service-list">
        <li class="service-item"><svg class="service-chevron" viewBox="0 0 52 60"><polyline points="-4,6 40,30 -4,54" fill="none" stroke="#f8ab17" stroke-width="13"/></svg><span class="service-name">Design</span></li>
        <li class="service-item"><svg class="service-chevron" viewBox="0 0 52 60"><polyline points="-4,6 40,30 -4,54" fill="none" stroke="#f8ab17" stroke-width="13"/></svg><span class="service-name">Engineering</span></li>
        <li class="service-item"><svg class="service-chevron" viewBox="0 0 52 60"><polyline points="-4,6 40,30 -4,54" fill="none" stroke="#f8ab17" stroke-width="13"/></svg><span class="service-name">Installation</span></li>
        <li class="service-item"><svg class="service-chevron" viewBox="0 0 52 60"><polyline points="-4,6 40,30 -4,54" fill="none" stroke="#f8ab17" stroke-width="13"/></svg><span class="service-name">Dismantling</span></li>
      </ul>
      <div class="brand"><span class="brand-square"></span><span class="brand-name">TRELBORN</span></div>
      <div class="sector-list"><span>COMMERCIAL</span><span>•</span><span>INDUSTRIAL</span><span>•</span><span>RESIDENTIAL</span><span>•</span><span>CIVIL</span></div>
    </section>
  </div>

  <p class="presentation-note">This Mock-Up is for presentation purposes only.</p>
</main>
</body>
</html>
```